Pricing Sheet for HVAC maintenance plan

I have a pricing sheet for our maintenance plan for my HVAC company. I want to have it put in a more appealing format than just a simple spreadsheet. I need it to be easy to read and yet exciting to look at.

Attached is the form in its word document. We need to have a signature line added as well.

Attached is also the company logo

Target Market(s)

Homeowners, both young and old

Industry/Entity Type

Hvac

Font styles to use
Serif

Colors
fbf289
ec1f27
faa54b
ffffff

Requirements
Must have
• Something that is easy to read.
• Must have logo
• Must have a signature and date line added
• Company colors - attached are some screenshots of what the color scheme might be. You can use this to draw inspiration
• Could be done on a dark background including black, as we paint our trucks black
Should not have
• Too much clutter.

```html
<!DOCTYPE html>
<html lang="en">
<head>
<meta charset="utf-8">
<title>Hearthline Climate Co. – Maintenance Plan Pricing</title>
<link rel="stylesheet" href="https://fonts.googleapis.com/css2?family=Barlow:wght@400;600&family=Tinos&display=swap">
<style>
:root{
  --brand-red:#a61c1c;
  --ink:#1e1e1e;
  --rule:#d6d6d6;
  --stripe:#efefef;
  --paper:#ffffff;
}
*{box-sizing:border-box;margin:0;padding:0}
html,body{width:773px;height:1200px;overflow:hidden;background:var(--paper)}
body{position:relative;font-family:"Barlow",Arial,sans-serif;color:var(--ink)}
.brand{position:absolute;top:80px;left:0;width:773px;display:flex;justify-content:center;align-items:center;gap:12px}
.brand-dot{width:22px;height:22px;border-radius:50%;background:var(--brand-red)}
.brand-name{font-size:32px;font-weight:600;color:var(--brand-red);letter-spacing:1px}
.licenses{position:absolute;left:43px;top:213px;font-size:12.5px;line-height:17px}
.divider{position:absolute;left:416px;top:200px;width:1.5px;height:78px;background:var(--ink)}
.contact{position:absolute;left:462px;top:213px;font-size:12.5px;line-height:17px}
.contact li{list-style:none;display:flex;align-items:center;gap:12px}
.contact svg{width:14px;height:14px;flex:none}
.contact .indent{padding-left:26px}
.customer{position:absolute;left:43px;top:300px;width:690px;display:grid;
  grid-template-columns:163px 246px 159px 122px;border-top:1px solid var(--rule);border-left:1px solid var(--rule)}
.customer div{height:30px;border-right:1px solid var(--rule);border-bottom:1px solid var(--rule);
  display:flex;align-items:center;gap:5px;padding-left:8px;font-size:14px}
.customer svg{width:14px;height:14px;flex:none}
.plan{position:absolute;left:43px;width:690px;display:grid;grid-template-columns:230px 230px 230px;border-left:1px solid var(--rule)}
.plan .head{height:28px;background:var(--brand-red);color:#fff;font-family:"Tinos","Times New Roman",serif;
  font-size:12.5px;display:flex;align-items:center;justify-content:center;border-right:1px solid #fff}
.plan .cell{height:28px;border-right:1px solid var(--rule);border-bottom:1px solid var(--rule);font-size:12px;display:flex;align-items:center;padding-left:7px}
.plan .alt{background:var(--stripe)}
.sign{position:absolute;left:43px;top:1121px;font-size:13px}
.date{position:absolute;left:489px;top:1139px;font-size:13px}
.line{display:inline-block;border-bottom:1px solid var(--ink);vertical-align:bottom}
</style>
</head>
<body>
<header class="brand"><span class="brand-dot"></span><span class="brand-name">HEARTHLINE CLIMATE CO.</span></header>

<div class="licenses">
  <p>NJ Electrical License #20451</p>
  <p>NJ Home Improvement Business Registration #13VH0918273</p>
  <p>NJ HVAC Lic # 394</p>
</div>
<div class="divider"></div>
<ul class="contact">
  <li><svg viewBox="0 0 14 14"><circle cx="7" cy="7" r="6" fill="none" stroke="#333"/><path d="M1 7h12M7 1c3 3 3 9 0 12M7 1c-3 3-3 9 0 12" fill="none" stroke="#333" stroke-width=".8"/></svg>www.HearthlineClimateCo.com</li>
  <li><svg viewBox="0 0 14 14"><circle cx="7" cy="7" r="6" fill="none" stroke="#333"/><rect x="4" y="5" width="6" height="4" fill="none" stroke="#333" stroke-width=".8"/><path d="M4 5l3 2 3-2" fill="none" stroke="#333" stroke-width=".8"/></svg>Info@HearthlineClimateCo.com</li>
  <li><svg viewBox="0 0 14 14"><path d="M2 3l5-1v10l-5 1zM7 2l5 1v10l-5-1z" fill="#333"/></svg>P.O.Box 512</li>
  <li class="indent">Brookvale, NJ, 07990</li>
</ul>

<section class="customer">
  <div><svg viewBox="0 0 14 14"><circle cx="7" cy="4" r="3" fill="#222"/><path d="M1 14c0-5 12-5 12 0z" fill="#222"/></svg>Name</div><div></div>
  <div><svg viewBox="0 0 14 14"><circle cx="7" cy="7" r="6" fill="none" stroke="#222"/><path d="M5 4l2 1-1 2 2 2 1-1 2 1-1 2c-3 0-6-3-6-6z" fill="#222"/></svg>Home Phone</div><div></div>
  <div><svg viewBox="0 0 14 14"><path d="M7 0a5 5 0 0 1 5 5c0 4-5 9-5 9S2 9 2 5a5 5 0 0 1 5-5z" fill="#222"/><circle cx="7" cy="5" r="2" fill="#fff"/></svg>Address</div><div></div>
  <div><svg viewBox="0 0 14 14"><rect x="4" y="1" width="7" height="12" rx="1" fill="none" stroke="#222" stroke-width="1.5"/></svg>Cell Phone</div><div></div>
  <div><svg viewBox="0 0 14 14"><path d="M1 13V6h3v7zM5 13V3h4v10zM10 13V7h3v6z" fill="#222"/></svg>City</div><div></div>
  <div><svg viewBox="0 0 14 14"><circle cx="7" cy="7" r="6" fill="none" stroke="#222"/><rect x="4" y="5" width="6" height="4" fill="none" stroke="#222" stroke-width=".8"/></svg>Email</div><div></div>
  <div><svg viewBox="0 0 14 14"><rect x="1" y="4" width="12" height="8" rx="1" fill="#222"/><rect x="1" y="6" width="12" height="1.5" fill="#fff"/></svg>Credit Card Number</div><div></div>
  <div><svg viewBox="0 0 14 14"><rect x="1" y="3" width="12" height="8" rx="1" fill="none" stroke="#222"/><rect x="1" y="5" width="12" height="1.3" fill="#222"/></svg>Expiration Date/CVV</div><div></div>
</section>

<section class="plan" style="top:442px">
  <div class="head">COMBINATION PACKAGES</div><div class="head">ASSURED PLAN</div><div class="head">PREFERRED PLAN</div>
  <div class="cell">A/C and Electric Heat</div><div class="cell"></div><div class="cell"></div>
  <div class="cell alt">A/C and Gas Furnace</div><div class="cell alt"></div><div class="cell alt"></div>
  <div class="cell">A/C and Boiler</div><div class="cell"></div><div class="cell"></div>
  <div class="cell alt">A/C and Oil Boiler</div><div class="cell alt"></div><div class="cell alt"></div>
  <div class="cell">Heat Pump</div><div class="cell"></div><div class="cell"></div>
</section>

<section class="plan" style="top:634px">
  <div class="head">SEPARATE SYSTEMS</div><div class="head">ASSURED PLAN</div><div class="head">PREFERRED PLAN</div>
  <div class="cell">A/C Only</div><div class="cell"></div><div class="cell"></div>
  <div class="cell alt">Gas Furnace Only</div><div class="cell alt"></div><div class="cell alt"></div>
  <div class="cell">Gas Boiler Only</div><div class="cell"></div><div class="cell"></div>
  <div class="cell alt">Oil Boiler</div><div class="cell alt"></div><div class="cell alt"></div>
</section>

<section class="plan" style="top:797px">
  <div class="head">OPTIONAL EQUIPMENT</div><div class="head">ASSURED PLAN</div><div class="head">PREFERRED PLAN</div>
  <div class="cell">Humidifier</div><div class="cell"></div><div class="cell"></div>
  <div class="cell alt">Electronic Air Cleaner</div><div class="cell alt"></div><div class="cell alt"></div>
  <div class="cell">Media Air Cleaner</div><div class="cell"></div><div class="cell"></div>
  <div class="cell alt">Attic Ventilation Fan</div><div class="cell alt"></div><div class="cell alt"></div>
  <div class="cell">Dehumidifier</div><div class="cell"></div><div class="cell"></div>
  <div class="head">ELECTRIC PLAN</div><div class="head">ASSURED PLAN</div><div class="head">PREFERRED PLAN</div>
  <div class="cell">Interior Electric</div><div class="cell"></div><div class="cell"></div>
  <div class="cell alt">Generator Maintenance Plan</div><div class="cell alt"></div><div class="cell alt"></div>
  <div class="cell">Prices are per month, per system</div><div class="cell"></div><div class="cell"></div>
</section>

<p class="sign">Signature: <span class="line" style="width:172px"></span></p>
<p class="date">Date:<span class="line" style="width:173px;margin-left:34px"></span></p>
</body>
</html>
```